Re-branding for Structural Engineering firm

We need new business cards as part of our current re-branding. We have a new logo (attached), so the card design should incorporate this color scheme. We are a structural engineering firm providing structural building design and seismic consulting services. The final design should communicate professionalism and stability, with a modern look and feel.

```html
<!DOCTYPE html>
<html lang="en">
<head>
<meta charset="utf-8">
<title>Northspan Engineering – Business Cards</title>
<link rel="stylesheet" href="https://fonts.googleapis.com/css2?family=Open+Sans:wght@600&family=Roboto:wght@300;400&display=swap">
<style>
  :root {
    --bg: #ececec;
    --blue: #4770b3;
    --blue-deep: #34517e;
    --blue-light: #4a74b4;
    --grey: #85868c;
    --ink: #333438;
    --text-soft: #6b6c70;
    --white: #ffffff;
  }
  * { margin: 0; padding: 0; box-sizing: border-box; }
  html, body { width: 1200px; height: 869px; overflow: hidden; }
  body {
    background: var(--bg);
    position: relative;
    font-family: "Roboto", Arial, sans-serif;
  }
  .card {
    position: absolute;
    top: 286px;
    width: 520px;
    height: 297px;
    overflow: hidden;
    box-shadow: 0 14px 30px rgba(0,0,0,0.18);
  }
  .card--front {
    left: 40px;
    background: radial-gradient(circle at 50% 50%, var(--blue-light) 0%, var(--blue-deep) 75%);
    display: flex;
    align-items: center;
    justify-content: center;
  }
  .brand {
    display: flex;
    align-items: center;
    gap: 14px;
    font-family: "Open Sans", Arial, sans-serif;
    font-weight: 600;
    color: var(--white);
  }
  .brand__mark { width: 46px; height: 46px; background: var(--white); }
  .brand__divider { width: 1px; height: 64px; background: var(--white); }
  .brand__name { font-size: 24px; line-height: 1.05; letter-spacing: 0.5px; }

  .card--back { left: 640px; background: var(--white); }
  .card__accent {
    position: absolute;
    left: 0;
    top: 0;
    width: 96px;
    height: 100%;
    background: linear-gradient(90deg, var(--blue) 0%, var(--blue) 55%, var(--grey) 100%);
  }
  .back-brand {
    position: absolute;
    left: 120px;
    top: 128px;
    display: flex;
    align-items: center;
    gap: 8px;
    font-family: "Open Sans", Arial, sans-serif;
    font-weight: 600;
    color: var(--blue);
  }
  .back-brand__mark { width: 26px; height: 26px; background: var(--blue); flex: none; }
  .back-brand__name { font-size: 13px; line-height: 1.1; letter-spacing: 0.3px; }
  .back-divider {
    position: absolute;
    left: 262px;
    top: 86px;
    width: 1.5px;
    height: 118px;
    background: var(--blue);
  }
  .contact { position: absolute; left: 280px; top: 80px; }
  .contact__name { font-size: 20px; font-weight: 400; color: var(--ink); letter-spacing: 0.3px; white-space: nowrap; }
  .contact__role { font-size: 13px; color: var(--blue); margin-top: 2px; }
  .contact__list { list-style: none; margin-top: 16px; }
  .contact__item {
    display: flex; align-items: center; gap: 8px;
    font-size: 12px; font-weight: 300; color: var(--text-soft);
    line-height: 18px; white-space: nowrap;
  }
  .contact__item svg { width: 11px; height: 11px; fill: var(--blue); flex: none; }
  .website {
    position: absolute;
    left: 330px;
    top: 236px;
    font-size: 12px;
    font-weight: 300;
    color: var(--text-soft);
  }
</style>
</head>
<body>
  <section class="card card--front" aria-label="Card front">
    <div class="brand">
      <span class="brand__mark"></span>
      <span class="brand__divider"></span>
      <span class="brand__name">NORTHSPAN<br>ENGINEERING</span>
    </div>
  </section>

  <section class="card card--back" aria-label="Card back">
    <div class="card__accent" role="img" aria-label="Decorative blue and grey accent band"></div>

    <div class="back-brand">
      <span class="back-brand__mark"></span>
      <span class="back-brand__name">NORTHSPAN<br>ENGINEERING</span>
    </div>

    <span class="back-divider"></span>

    <div class="contact">
      <p class="contact__name">DANA WHITFORD, S.E.</p>
      <p class="contact__role">Principal</p>
      <ul class="contact__list">
        <li class="contact__item">
          <svg viewBox="0 0 12 12"><path d="M6 0a4 4 0 0 0-4 4c0 3 4 8 4 8s4-5 4-8a4 4 0 0 0-4-4zm0 5.5A1.5 1.5 0 1 1 6 2.5a1.5 1.5 0 0 1 0 3z"/></svg>
          450 Harbor Ave
        </li>
        <li class="contact__item">
          <svg viewBox="0 0 12 12"><path d="M2.5 0.5l2 2.2-1 1.5c.8 1.6 2 2.8 3.6 3.6l1.5-1 2.2 2-1.3 2.4C5 10.8 1.2 7 0.1 1.8z"/></svg>
          555.210.4417, 555.380.9126
        </li>
        <li class="contact__item">
          <svg viewBox="0 0 12 12"><path d="M0 2h12v8H0z"/></svg>
          dana@northspanse.com
        </li>
      </ul>
    </div>

    <p class="website">www.northspanse.com</p>
  </section>
</body>
</html>
```